RW Frameworks Inc Business cards

We need business cards using our existing logo but slightly modified. Right now the logo says RW Framework Masonry. We want to keep the RW part of the design, but replace the Framework Masonry portion with "FRAMEWORKS". Please see the attached file.
Ideally this would be a blank template so we can add Different Names, titles, and phone numbers later.
On the one side we want only the logo and on the other side the detail. I'm attaching an example for you to see.
Please reach out with any other questions. Our address and other details will be given out once we find a design we like.

Target Market(s)

Construction Industry

```html
<!DOCTYPE html>
<html lang="en">
<head>
<meta charset="utf-8">
<title>RW Frameworks Inc – Business Cards</title>
<link href="https://fonts.googleapis.com/css2?family=Roboto+Condensed:wght@300;400;700&display=swap" rel="stylesheet">
<style>
  :root {
    --stage-blue: #2a7fe8;
    --card-dark: #262626;
    --card-light: #ffffff;
    --brand-blue: #1f73c4;
    --text-light: #f2f2f2;
    --text-muted: #d6d6d6;
    --logo-dark: #1f73c4;
  }
  * { box-sizing: border-box; margin: 0; padding: 0; }
  html, body { width: 1200px; height: 900px; overflow: hidden; }
  body {
    background: var(--stage-blue);
    font-family: "Roboto Condensed", Arial, sans-serif;
    position: relative;
  }
  .card {
    position: absolute;
    top: 302px;
    width: 520px;
    height: 297px;
    overflow: hidden;
    box-shadow: 0 18px 40px rgba(0, 30, 90, 0.35);
  }
  .card--front { left: 50px; background: var(--card-dark); }
  .card--back { left: 630px; background: var(--card-dark); }

  /* front */
  .world-texture {
    position: absolute;
    left: 60px; top: 40px; width: 400px; height: 220px;
    background: radial-gradient(ellipse at center, rgba(255,255,255,0.05), rgba(255,255,255,0) 70%);
  }
  .brand-name {
    position: absolute;
    left: 0; right: 0; top: 50%;
    transform: translateY(-50%);
    text-align: center;
    font-weight: 700;
    font-size: 46px;
    letter-spacing: 4px;
    color: var(--text-light);
    text-transform: uppercase;
  }

  /* back */
  .back-logo-panel {
    position: absolute;
    left: 0; top: 0; bottom: 0; width: 200px;
    background: var(--card-light);
  }
  .back-logo-panel .brand-name {
    font-size: 24px;
    letter-spacing: 2px;
    color: var(--logo-dark);
  }
  .contact-pill {
    position: absolute;
    left: 182px; top: 116px;
    width: 36px; height: 150px;
    border-radius: 18px;
    background: var(--brand-blue);
    display: flex; flex-direction: column;
    align-items: center; justify-content: space-around;
    padding: 12px 0;
  }
  .contact-pill svg { width: 15px; height: 15px; }
  .details {
    position: absolute;
    left: 250px; top: 48px;
    color: var(--text-light);
  }
  .details__name { font-weight: 300; font-size: 28px; line-height: 1; }
  .details__title { font-weight: 300; font-size: 12px; color: var(--brand-blue); margin-top: 4px; }
  .details__group { margin-top: 20px; font-size: 12px; font-weight: 400; line-height: 1.45; color: var(--text-muted); }
</style>
</head>
<body>

<section class="card card--front" aria-label="Business card front">
  <div class="world-texture" role="img" aria-label="Faint world map texture behind the logo"></div>
  <p class="brand-name">RW Frameworks</p>
</section>

<section class="card card--back" aria-label="Business card back">
  <div class="back-logo-panel">
    <p class="brand-name">RW Frameworks</p>
  </div>

  <div class="contact-pill">
    <svg viewBox="0 0 16 16" fill="none" stroke="#fff" stroke-width="1.2" aria-label="Web">
      <circle cx="8" cy="8" r="6.5"/><ellipse cx="8" cy="8" rx="3" ry="6.5"/><path d="M1.5 8h13M2.5 4.8h11M2.5 11.2h11"/>
    </svg>
    <svg viewBox="0 0 16 16" fill="none" stroke="#fff" stroke-width="1.2" aria-label="Address">
      <path d="M8 15s-5-5-5-8.5a5 5 0 0 1 10 0C13 10 8 15 8 15z"/><circle cx="8" cy="6.5" r="1.8"/>
    </svg>
    <svg viewBox="0 0 16 16" fill="none" stroke="#fff" stroke-width="1.2" aria-label="Phone">
      <path d="M4 1.8l2 3-1.3 1.3a8 8 0 0 0 5.2 5.2L11.2 10l3 2-1.2 2.2C7.5 14.5 1.5 8.5 1.8 3z"/>
    </svg>
  </div>

  <div class="details">
    <p class="details__name">Daniel Whitford</p>
    <p class="details__title">Chief Executive Officers</p>
    <p class="details__group">daniel@rwframeworks.com<br>www.rwframeworks.com</p>
    <p class="details__group">41 Granite Avenue, 3rd Floor<br>Springvale, ST - 40125</p>
    <p class="details__group">00 (555) 0142 730 (Fax)<br>00 (555) 0198 264 (Mobile)</p>
  </div>
</section>

</body>
</html>
```